Business card design for engineering firm specializing in defense industry.

We need a professional business card design. Something simple but stands out. We are an engineering company specializing in composites in the defense industry.
Industry/Entity Type
Defense
Contact Information for Business Card
A simple black business card with the Varlonix yellow color is what we had in mind but open for other designs.
Colors
ffc214

```html
<!DOCTYPE html>
<html lang="en">
<head>
<meta charset="utf-8">
<title>Varlonix Business Card</title>
<link rel="stylesheet" href="https://fonts.googleapis.com/css2?family=Archivo+Black&family=Michroma&family=Exo+2:wght@500&display=swap">
<style>
  :root {
    --brand-yellow: #ffc214;
    --ink-black: #0c0c0c;
    --paper-white: #ffffff;
    --stage-grey: #2a2a2a;
    --steel-light: #9a9a9a;
  }
  * { box-sizing: border-box; margin: 0; padding: 0; }
  html, body { width: 1200px; height: 903px; overflow: hidden; }
  body {
    background: var(--stage-grey);
    position: relative;
    font-family: "Archivo Black", sans-serif;
  }
  .card {
    position: absolute;
    width: 520px;
    height: 300px;
    border-radius: 22px;
    overflow: hidden;
    top: 301px;
  }
  /* Back side */
  .card--back {
    left: 50px;
    background: var(--brand-yellow);
  }
  .card--back .wordmark {
    position: absolute;
    left: 0; right: 0;
    top: 104px;
    text-align: center;
    font-size: 54px;
    color: var(--ink-black);
    letter-spacing: 1px;
  }
  .card--back .website {
    position: absolute;
    left: 0; right: 0;
    top: 196px;
    text-align: center;
    font-family: "Michroma", sans-serif;
    font-size: 13px;
    letter-spacing: 3px;
    color: var(--ink-black);
  }
  /* Front side */
  .card--front {
    left: 630px;
    background: var(--paper-white);
  }
  .front-band-top {
    position: absolute;
    left: 0; top: 0;
    width: 370px; height: 72px;
    background: var(--brand-yellow);
    padding: 16px 0 0 26px;
    color: var(--ink-black);
  }
  .holder-name { font-size: 19px; letter-spacing: 0.5px; line-height: 1.1; }
  .holder-role { font-size: 11px; letter-spacing: 0.5px; margin-top: 4px; }
  .front-band-bottom {
    position: absolute;
    left: 0; bottom: 0;
    width: 100%; height: 78px;
    background: var(--ink-black);
    padding: 15px 0 0 26px;
    color: var(--paper-white);
    font-family: "Exo 2", sans-serif;
    font-weight: 500;
    font-size: 16px;
    letter-spacing: 0.5px;
  }
  .contact-line { display: flex; align-items: center; gap: 10px; height: 24px; }
  .contact-line svg { width: 15px; height: 15px; flex: none; }
  .feature-panel {
    position: absolute;
    right: 0; top: 0;
    width: 150px; height: 222px;
    background: linear-gradient(135deg, #0c0c0c 0%, #3a3a3a 45%, #d8d8d8 70%, #1a1a1a 100%);
  }
  .card--front .wordmark {
    position: absolute;
    left: 26px;
    top: 102px;
    font-size: 46px;
    color: var(--ink-black);
    letter-spacing: 1px;
  }
  .card--front .website {
    position: absolute;
    left: 26px;
    top: 172px;
    font-family: "Michroma", sans-serif;
    font-size: 12px;
    letter-spacing: 2.5px;
    color: var(--ink-black);
  }
</style>
</head>
<body>
  <section class="card card--back" aria-label="Card back">
    <div class="wordmark">Varlonix</div>
    <div class="website">WWW.VARLONIX.COM</div>
  </section>

  <section class="card card--front" aria-label="Card front">
    <div class="front-band-top">
      <div class="holder-name">DANIEL MORROW</div>
      <div class="holder-role">CEO/FOUNDER</div>
    </div>
    <div class="feature-panel" role="img" aria-label="Decorative black and silver brand graphic"></div>
    <div class="wordmark">Varlonix</div>
    <div class="website">WWW.VARLONIX.COM</div>
    <div class="front-band-bottom">
      <div class="contact-line">
        <svg viewBox="0 0 24 24" aria-hidden="true"><path fill="var(--brand-yellow)" d="M6.6 10.8a15.1 15.1 0 0 0 6.6 6.6l2.2-2.2a1 1 0 0 1 1-.25 11.4 11.4 0 0 0 3.6.57 1 1 0 0 1 1 1V20a1 1 0 0 1-1 1A17 17 0 0 1 3 4a1 1 0 0 1 1-1h3.5a1 1 0 0 1 1 1c0 1.25.2 2.45.57 3.57a1 1 0 0 1-.25 1z"/></svg>
        <span>555.014.2270</span>
      </div>
      <div class="contact-line">
        <svg viewBox="0 0 24 24" aria-hidden="true"><rect x="2" y="5" width="20" height="14" fill="var(--brand-yellow)"/><path d="M2 5l10 8 10-8" fill="none" stroke="var(--ink-black)" stroke-width="1.6"/></svg>
        <span>daniel@varlonix.com</span>
      </div>
    </div>
  </section>
</body>
</html>
```